Flyer-Design für Unternehmensberatung für Potenzialentfaltung
Zielgruppe
Wir sind eine kleine Unternehmensberatung für Potenzialentfaltung (https://furemi.de) und unterstützen Menschen in Unternehmen ihre Zusammenarbeit zu verbessern.
Für das vorliegende Projekt ist die Zielgruppe Führungskräfte, die in einem 12 Wochen Peer-Coaching Programm (https://team-impuls-werkstatt.de) ihre Führungskompetenzen selbst mit Hilfe von Themen-Guides in kleinen Führungscircles weiterentwickeln können.
Aufgabenstellung
Zur Ansprache unserer Kunden benötigen wir einen One-Pager, der im wesentlichen die Landingpage (https://team-impuls-werkstatt.de) auf eine DIN A4 -Seite abbildet.
Damit wir die in Kürze folgenden Anpassungen einfach selbst durchführen können, möchten wir diesen DIN A4 Onepager in dem Powerpoint-Format .pptx erstellt haben.

```html
<!DOCTYPE html>
<html lang="de">
<head>
<meta charset="utf-8">
<title>Team Impuls Werkstatt – Flyer</title>
<link rel="stylesheet" href="https://fonts.googleapis.com/css2?family=Montserrat:wght@400;500;600;700&display=swap">
<style>
  :root {
    --stage: #bdbdbd;
    --paper: #ffffff;
    --blue: #1b9ad6;
    --blue-light: #49b3e3;
    --blue-dark: #0a85c2;
    --grey-text: #8a8a8a;
    --grey-head: #8f8f8f;
    --grey-band: #ebebeb;
    --ink: #444444;
  }
  * { box-sizing: border-box; margin: 0; padding: 0; }
  html, body { width: 1058px; height: 1200px; overflow: hidden; background: var(--stage); }
  body { font-family: "Montserrat", sans-serif; }
  .flyer {
    position: absolute; left: 105px; top: 0;
    width: 848px; height: 1200px; background: var(--paper); overflow: hidden;
  }
  .hero { position: absolute; left: 0; top: 0; width: 848px; height: 312px; }
  .hero-photo {
    position: absolute; inset: 0;
    background: linear-gradient(100deg, #1596d4 0%, #2aa7e0 45%, #6fc0e6 70%, #8fb3c6 100%);
  }
  .brand { position: absolute; left: 41px; top: 26px; display: flex; align-items: center; gap: 14px; }
  .brand-mark { width: 72px; height: 72px; background: #fff; border-radius: 12px; }
  .brand-name { color: #fff; font-weight: 700; font-size: 30px; line-height: 1.1; }
  .hero-title { position: absolute; left: 41px; top: 118px; color: #fff; font-weight: 600; font-size: 33px; }
  .hero-lead { position: absolute; left: 43px; top: 170px; color: #fff; font-weight: 600; font-size: 13.5px; line-height: 1.4; }
  .hero-question { position: absolute; left: 43px; top: 240px; color: #fff; font-weight: 600; font-size: 20px; }
  .hero-result { position: absolute; left: 43px; top: 272px; color: #fff; font-weight: 500; font-size: 12.5px; }
  .hero-result b { font-weight: 700; }

  .questions { position: absolute; left: 0; top: 312px; width: 848px; height: 183px; }
  .question { position: absolute; left: 42px; display: flex; align-items: flex-start; gap: 16px; }
  .question svg { flex: none; }
  .question p { font-size: 12px; line-height: 1.45; color: var(--ink); font-weight: 500; }
  .bee-scene {
    position: absolute; left: 499px; top: 6px; width: 300px; height: 172px;
    background: linear-gradient(135deg, #f4f4f1, #ece6d6);
  }

  .purpose { position: absolute; left: 0; top: 495px; width: 848px; height: 180px; background: var(--blue-light); }
  .purpose-photo {
    position: absolute; left: 0; top: 0; width: 431px; height: 180px;
    background: linear-gradient(90deg, #3f8fbf, #7fbfdf 60%, #a9d5ea);
  }
  .purpose-text { position: absolute; left: 439px; top: 8px; width: 400px; color: #fff; }
  .purpose-text h2 { font-size: 19px; font-weight: 600; line-height: 1.3; margin-bottom: 6px; }
  .purpose-text p { font-size: 11.2px; line-height: 1.5; font-weight: 500; }

  .explain { position: absolute; top: 688px; width: 380px; }
  .explain h2 { font-size: 19px; font-weight: 600; color: var(--grey-head); line-height: 1.3; margin-bottom: 8px; }
  .explain p { font-size: 11.6px; line-height: 1.5; color: var(--grey-text); font-weight: 500; }
  .explain-what { left: 43px; }
  .explain-how { left: 439px; }

  .offer { position: absolute; left: 0; top: 869px; width: 848px; height: 331px; background: var(--grey-band); }
  .offer h2 { position: absolute; top: 16px; width: 100%; text-align: center; font-size: 19px; font-weight: 600; color: var(--grey-head); }
  .offer-intro { position: absolute; top: 52px; left: 60px; width: 728px; text-align: center; font-size: 11.2px; line-height: 1.5; color: var(--grey-text); font-weight: 500; }
  .card {
    position: absolute; top: 112px; width: 112px; height: 161px; background: #fff;
    box-shadow: 0 1px 4px rgba(0,0,0,0.25); text-align: center; padding: 0 6px;
  }
  .card-icon { width: 80px; height: 80px; margin: 8px auto 12px; border-radius: 6px; }
  .card h3 { font-size: 9.5px; font-weight: 700; color: var(--blue); line-height: 1.3; margin-bottom: 4px; }
  .card p { font-size: 7.5px; line-height: 1.5; color: var(--ink); }
  .footer-bar {
    position: absolute; left: 141px; top: 292px; width: 554px; height: 36px; background: var(--blue-dark);
    color: #fff; font-size: 13px; font-weight: 600; display: flex; align-items: center; justify-content: center;
  }
</style>
</head>
<body>
<main class="flyer">
  <section class="hero">
    <div class="hero-photo" role="img" aria-label="Foto: lächelnde Gruppe von Geschäftsleuten in blauer Tönung"></div>
    <div class="brand">
      <div class="brand-mark"></div>
      <div class="brand-name">Team Impuls<br>Werkstatt</div>
    </div>
    <h1 class="hero-title">Bienenhirte oder Leadership?</h1>
    <p class="hero-lead">Wir unterstützen dich dabei, dein Führungsverhalten in<br>komplexen Veränderungsvorhaben selbst zu entwickeln<br>und dein volles Potenzial als Leader zu entfalten!</p>
    <p class="hero-question">Nimmst du die Challenge an?</p>
    <p class="hero-result"><b>Resultat:</b> Mehr Wertschätzung, mehr Wertschöpfung und mehr Spaß!</p>
  </section>

  <section class="questions">
    <div class="question" style="top:14px">
      <svg width="30" height="30" viewBox="0 0 30 30"><circle cx="15" cy="15" r="15" fill="#49b3e3"/><text x="15" y="21" text-anchor="middle" font-family="Montserrat, sans-serif" font-weight="700" font-size="18" fill="#fff">?</text></svg>
      <p>Bist du ein/e Bienenhirte/-hirtin und versuchst<br>mit alten Führungsprinzipien in selbstorganisierten<br>Teams oder Unternehmen erfolgreich zu sein?</p>
    </div>
    <div class="question" style="top:80px">
      <svg width="30" height="30" viewBox="0 0 30 30"><circle cx="15" cy="15" r="15" fill="#49b3e3"/><text x="15" y="21" text-anchor="middle" font-family="Montserrat, sans-serif" font-weight="700" font-size="18" fill="#fff">?</text></svg>
      <p>Wie gelingt es dir deine selbstorganisierten<br>Teams erfolgreich zu unterstützen?</p>
    </div>
    <div class="question" style="top:130px">
      <svg width="30" height="30" viewBox="0 0 30 30"><circle cx="15" cy="15" r="15" fill="#49b3e3"/><text x="15" y="21" text-anchor="middle" font-family="Montserrat, sans-serif" font-weight="700" font-size="18" fill="#fff">?</text></svg>
      <p>Wie kannst du und deine Organisation mit der<br>wachsenden Komplexität wertschöpfend umgehen?</p>
    </div>
    <div class="bee-scene" role="img" aria-label="Zeichnung: ratloser Hirte mit Bienenkorb, Bienen und schlafendem Hund"></div>
  </section>

  <section class="purpose">
    <div class="purpose-photo" role="img" aria-label="Foto: Team im Gespräch in blauer Tönung"></div>
    <div class="purpose-text">
      <h2>Wozu dient diese Team Impuls<br>Werkstatt?</h2>
      <p>Sie dient einer evolutionären Organisationsentwicklung, in der die Menschen und die Teams selbstorganisiert jeden Tag die richtigen Dinge mit Freude gemeinsam richtig tun. Es geht darum Kunden besser zu versorgen, allen Mitarbeitenden ein zufriedenstellenderes Arbeiten zu ermöglichen und dabei ansehnliche Profite zu erwirtschaften.</p>
    </div>
  </section>

  <section class="explain explain-what">
    <h2>Was ist eine Team Impuls<br>Werkstatt?</h2>
    <p>Es ist eine Herausforderung für dich als Führungskraft, dich in einem Circle mit 2–4 Anderen auf Augenhöhe 12 Wochen lang einem Führungsthema in deiner Selbst-Entwicklung zu stellen. Einmal pro Woche arbeitet ihr gemeinsam anhand eines Circle-Guides an euren Führungsthemen.</p>
  </section>
  <section class="explain explain-how">
    <h2>Wie funktioniert eine Team Impuls<br>Werkstatt?</h2>
    <p>In dem geschützten Raum deines Circles arbeitest du 12 Wochen an deinem selbstgewählten Thema. In euren Circlemeetings unterstützt ihr euch gegenseitig bei eurer Selbst-Entwicklung. Die themenspezifischen Circle-Guides geben euch Leitplanken und helfen euch bei der Entfaltung eures vollen Potenzials.</p>
  </section>

  <section class="offer">
    <h2>Unser Angebot</h2>
    <p class="offer-intro">Unser Team unterstützt dich oder deine Organisation in Veränderungsvorhaben, um die Team Impuls Werkstatt (TIW) einzuführen oder mit Coaching und Mentoring zu begleiten. In einer individuellen Beratung klären wir, welche Möglichkeiten die Einladung zu einer TIW im Hinblick auf eure Organisationsentwicklung bietet.</p>

    <div class="card" style="left:127px">
      <div class="card-icon" role="img" aria-label="Symbolbild: Rakete" style="background:#dce9f2"></div>
      <h3>TIW - Startup<br>Support</h3>
      <p>Im Idealfall beginnt die TIW mit einem Open Space Event</p>
    </div>
    <div class="card" style="left:287px">
      <div class="card-icon" role="img" aria-label="Symbolbild: Personenkreis" style="background:#f1e3e3"></div>
      <h3>TIW - Coaching</h3>
      <p>Coaching eines Circles/einer Organisation für 12 Wochen</p>
    </div>
    <div class="card" style="left:446px">
      <div class="card-icon" role="img" aria-label="Symbolbild: Mentor hilft auf Treppe" style="background:#e3efe0"></div>
      <h3>TIW - Mentoring</h3>
      <p>Begleitung von Moderatoren und Circle-Meetings</p>
    </div>
    <div class="card" style="left:606px">
      <div class="card-icon" role="img" aria-label="Symbolbild: Beratungsgespräch" style="background:#f3ecd9"></div>
      <h3>TIW - Beratung</h3>
      <p>Ganzheitlicher Blick auf Veränderungsvorhaben</p>
    </div>

    <div class="footer-bar">FUREMI GmbH | team-impuls-werkstatt.de | kontakt@furemi.de</div>
  </section>
</main>
</body>
</html>
```